Mirabo & Orvan Automotive Repair Shop. Need a new website design.

We specialize in Mirabo & Orvan auto repair, but also work on other Asian import vehicles. We have been in business for 7 years and pride ourselves on high quality auto repair that is fixed right the first time. Would like the automotive repair website to incorporate the colors black, red and white if possible and have our logo and some Mirabo and Orvan vehicles included in the website.

Target Market(s)

Mirabo & Orvan vehicle owners

Industry/Entity Type

Automotive Repair

Coding

Coded - Design and coding required

Number of Pages Required

5+ page

Colors
EB3D1F
EC4F4E
F09395
F8D3D4
FCEDEE

Requirements
Must have
• Home, Services, Contact Us, Schedule appointment, and a gallery tab that I can add shop pictures to when completed.
Nice to have
• Would like to see example pictures of job next to each service listed.
Should not have
• Service not related to auto repair. Ex. auto detailing, towing, car wash

```html
<!DOCTYPE html>
<html lang="en">
<head>
<meta charset="utf-8">
<title>Varro Automotive</title>
<link href="https://fonts.googleapis.com/css2?family=Unbounded:wght@700;800&family=Poppins:wght@400;500;600;700&display=swap" rel="stylesheet">
<style>
:root{
  --red:#EB3D1F;--red2:#EC4F4E;--pink:#F09395;--blush:#F8D3D4;--cream:#FCEDEE;
  --black:#0b0b0b;--ink:#111;--white:#fff;--grey:#555;
}
*{box-sizing:border-box;margin:0;padding:0}
html,body{width:1200px;height:5103px;overflow:hidden}
body{position:relative;font-family:"Poppins",sans-serif;color:var(--ink);background:var(--white)}
.abs{position:absolute}
.head{font-family:"Unbounded",sans-serif;font-weight:800}
.btn{position:absolute;display:flex;align-items:center;justify-content:center;gap:14px;font-size:12px;font-weight:600}
.btn svg{width:26px;height:10px}
.btn-dark{background:var(--black);color:#fff}
.btn-light{background:#fff;color:var(--ink)}
.btn-red{background:var(--red);color:#fff}
.photo{position:absolute}
/* hero */
.hero{position:absolute;left:0;top:0;width:1200px;height:750px;background:linear-gradient(100deg,#121212 0%,#2a2a2a 45%,#4a4a4a 70%,#2b2b2b 100%)}
.topbar{position:absolute;left:0;top:0;width:1200px;height:44px;background:rgba(0,0,0,.35);color:#ddd;font-size:11px}
.navbar{position:absolute;left:0;top:44px;width:1200px;height:76px;background:rgba(0,0,0,.45)}
.logo{position:absolute;left:125px;top:0;width:208px;height:180px;display:flex;align-items:center;justify-content:center;gap:10px}
.logo .sq{width:22px;height:22px;background:var(--red)}
.logo span{font-family:"Unbounded",sans-serif;font-weight:800;font-size:32px;color:#fff}
.nav a{position:absolute;top:74px;color:#fff;font-size:12px;text-decoration:none}
.hero h1{position:absolute;left:125px;top:300px;width:620px;font-size:42px;line-height:56px;color:#fff}
.hero p{position:absolute;left:125px;top:433px;width:470px;font-size:12px;line-height:20px;color:#ddd}
/* about */
.about{position:absolute;left:0;top:750px;width:1200px;height:620px;background:var(--cream)}
.about .eyebrow{position:absolute;right:128px;top:850px;color:var(--red);font-size:13px;font-weight:600}
.about-title{position:absolute;right:128px;top:868px;text-align:right;font-size:40px;line-height:54px}
.about-text{position:absolute;right:128px;top:995px;width:420px;text-align:right;font-size:12px;line-height:20px;color:#333}
/* elevate */
.elevate-title{position:absolute;left:0;top:1470px;width:1200px;text-align:center;font-size:40px;line-height:56px}
.pager{position:absolute;font-size:12px;font-weight:600;display:flex;gap:34px}
.pager .prev{border-bottom:1.5px solid var(--ink);padding-bottom:3px}
.pager .next{color:var(--red);border-bottom:1.5px solid var(--red);padding-bottom:3px}
/* services */
.services{position:absolute;left:0;top:2180px;width:1200px;height:605px;background:var(--cream)}
.eyebrow-sm{position:absolute;color:var(--red);font-size:13px;font-weight:600}
.sec-title{position:absolute;font-size:42px;letter-spacing:2px}
.card{position:absolute;top:2472px;height:214px;background:#fff;box-shadow:0 4px 14px rgba(0,0,0,.08)}
.card .pic{position:absolute;left:40px;right:40px;top:0;height:96px}
.card h3{position:absolute;left:40px;top:112px;font-size:16px;font-weight:700}
.card p{position:absolute;left:40px;top:140px;width:220px;font-size:10px;line-height:16px;color:#444}
.card a{position:absolute;left:40px;top:180px;font-size:10px;color:var(--red);font-weight:600;display:flex;gap:10px;align-items:center}
/* gallery */
.center-text{position:absolute;left:0;width:1200px;text-align:center}
/* contact */
.contact{position:absolute;left:0;top:3797px;width:1200px;height:698px;background:linear-gradient(110deg,#151515 0%,#2e2e2e 40%,#4d4d4d 75%,#222 100%)}
.form{position:absolute;left:528px;top:3897px;width:555px;height:514px;background:var(--red)}
.form h2{position:absolute;left:44px;top:38px;color:#fff;font-size:36px}
.field{position:absolute;left:44px;width:466px;height:40px;background:#fff;font-size:10px;color:#555;padding:10px 16px}
.partners{position:absolute;left:0;top:4495px;width:1200px;height:145px;background:#fff}
.badge{position:absolute;top:4535px;height:66px}
/* footer */
.footer{position:absolute;left:0;top:4640px;width:1200px;height:407px;background:var(--black);color:#fff}
.footer h4{position:absolute;top:100px;font-size:18px;font-weight:600}
.footer ul{position:absolute;top:150px;list-style:none;font-size:11px;line-height:36px;color:#ddd}
.footer li{display:flex;align-items:center;gap:10px}
.dot{width:10px;height:10px;border-radius:50%;background:var(--red);display:inline-block}
.copy{position:absolute;left:0;top:5047px;width:1200px;height:56px;line-height:56px;text-align:center;font-size:11px;color:#333}
</style>
</head>
<body>

<!-- HERO -->
<section class="hero">
  <div class="photo" role="img" aria-label="Mechanic working with a wrench under an open car hood" style="left:560px;top:0;width:640px;height:750px;background:radial-gradient(ellipse at 60% 45%,#8a8a8a 0%,#4a4a4a 45%,rgba(30,30,30,0) 80%)"></div>
  <div class="topbar">
    <span class="abs" style="left:594px;top:14px">We're Open Mon - Sat 8:00 - 11:00</span>
    <span class="abs" style="left:862px;top:14px">Follow Us On</span>
    <span class="abs dot" style="left:960px;top:17px;background:#ccc"></span>
    <span class="abs dot" style="left:994px;top:17px;background:#ccc"></span>
    <span class="abs dot" style="left:1028px;top:17px;background:#ccc"></span>
    <span class="abs dot" style="left:1062px;top:17px;background:#ccc"></span>
  </div>
  <div class="navbar"></div>
  <div class="logo" style="background:var(--black)"><div class="sq"></div><span>VARRO</span></div>
  <nav class="nav">
    <a style="left:416px">Home</a><a style="left:496px">Services</a><a style="left:587px">Gallery</a><a style="left:673px">Contact Us</a><a style="left:784px">Schedule appointment</a>
  </nav>
  <svg class="abs" style="left:1012px;top:72px" width="20" height="20" viewBox="0 0 20 20" fill="none" stroke="#fff" stroke-width="2"><circle cx="8" cy="8" r="6"/><path d="M13 13l5 5"/></svg>
  <svg class="abs" style="left:1052px;top:72px" width="22" height="20" viewBox="0 0 22 20" fill="none" stroke="#fff" stroke-width="2"><path d="M1 2h4l3 11h11l2-8H7"/><circle cx="9" cy="17" r="1.5"/><circle cx="18" cy="17" r="1.5"/></svg>
  <h1 class="head">We Fix, You Drive with Confidence.</h1>
  <p>Lorem Ipsum is simply dummy text of the printing and typesetting industry. Lorem Ipsum has been the industry's standard dummy text ever since the 1500s</p>
  <div class="btn btn-light" style="left:125px;top:533px;width:250px;height:38px">Schedule Appointment <svg viewBox="0 0 26 10" fill="none" stroke="#111" stroke-width="1.5"><path d="M0 5h24M20 1l4 4-4 4"/></svg></div>
</section>

<!-- ABOUT -->
<section class="about">
  <svg class="abs" style="left:0;top:0" width="640" height="620" role="img" aria-label="Silver sedan parked on a driveway with a video play button">
    <defs><linearGradient id="carg" x1="0" y1="0" x2="1" y2="1"><stop offset="0" stop-color="#6f8a86"/><stop offset=".5" stop-color="#a9c4c0"/><stop offset="1" stop-color="#5d6b6a"/></linearGradient></defs>
    <polygon points="0,0 485,0 640,620 0,620" fill="url(#carg)"/>
    <circle cx="280" cy="310" r="50" fill="rgba(235,61,31,.35)"/>
    <circle cx="280" cy="310" r="34" fill="var(--red)"/>
    <circle cx="280" cy="310" r="22" fill="none" stroke="#fff" stroke-width="2"/>
    <path d="M274 300 L290 310 L274 320 Z" fill="#fff"/>
  </svg>
</section>
<div class="about-wrap">
  <span class="about eyebrow" style="all:unset;position:absolute;right:128px;top:848px;color:var(--red);font-size:13px;font-weight:600;font-family:Poppins,sans-serif">ABOUT</span>
  <h2 class="about-title head">Varro<br>Automotive</h2>
  <p class="about-text">Led by an NAT master certified technician with 20 years experience working for Mirabo &amp; Orvan dealerships, our auto shop is your go to facility for everything from factory-auto maintenance, including oil changes, fluid services and tune ups, to complex engine repairs, hybrid diagnostic &amp; repair, brake jobs, etc. We have state of the art equipment and tools to ensure that we can properly diagnose and repair your vehicle to get you back on the road quickly. Our work comes with a warranty and we offer towing if needed. We also offer discounts for RideGo &amp; Hopcar rides.</p>
  <div class="btn btn-dark" style="left:908px;top:1230px;width:167px;height:40px">Learn More <svg viewBox="0 0 26 10" fill="none" stroke="#fff" stroke-width="1.5"><path d="M0 5h24M20 1l4 4-4 4"/></svg></div>
</div>

<!-- SPECIALIZED REPAIRS -->
<h2 class="elevate-title head">Elevate Your Drive With<br>Specialized Repairs</h2>
<div class="photo" role="img" aria-label="Grey sedan in a garage" style="left:0;top:1680px;width:200px;height:330px;background:linear-gradient(135deg,#cfcfcf,#8d8d8d)"></div>
<div class="photo" role="img" aria-label="Dark sedan parked outdoors" style="left:200px;top:1680px;width:200px;height:330px;background:linear-gradient(135deg,#9a9a9a,#5e5e5e)"></div>
<div class="photo" role="img" aria-label="Blue crossover in a parking lot" style="left:800px;top:1680px;width:200px;height:330px;background:linear-gradient(135deg,#c9d1d8,#7b8a96)"></div>
<div class="photo" role="img" aria-label="Silver SUV at a dealership" style="left:1000px;top:1680px;width:200px;height:330px;background:linear-gradient(135deg,#e0e4e8,#9ea7ae)"></div>
<div class="abs" style="left:545px;top:1632px;width:266px;height:40px;background:var(--red)"></div>
<div class="abs" style="left:387px;top:1900px;width:266px;height:156px;background:var(--red)"></div>
<div class="photo" role="img" aria-label="Black Orvan SUV front view" style="left:403px;top:1645px;width:397px;height:397px;background:linear-gradient(160deg,#4a4a4a 0%,#262626 55%,#111 100%)"></div>
<div class="abs head" style="left:403px;top:1870px;width:397px;text-align:center;color:#fff;font-size:34px;letter-spacing:2px">ORVAN</div>
<div class="pager" style="left:908px;top:2060px"><span class="prev">Prev</span><span class="next">Next</span></div>

<!-- SERVICES -->
<section class="services"></section>
<span class="eyebrow-sm" style="left:125px;top:2282px">OUR</span>
<h2 class="sec-title head" style="left:125px;top:2300px">SERVICES</h2>
<p class="abs" style="left:125px;top:2370px;width:380px;font-size:12px;line-height:20px;color:#333">Lorem Ipsum is simply dummy text of the printing and typesetting industry. Lorem Ipsum has been the industry's standard dummy text ever since the 1500</p>
<div class="btn btn-dark" style="left:908px;top:2338px;width:167px;height:38px">View All <svg viewBox="0 0 26 10" fill="none" stroke="#fff" stroke-width="1.5"><path d="M0 5h24M20 1l4 4-4 4"/></svg></div>
<div class="pager" style="left:908px;top:2402px"><span class="prev">Prev</span><span class="next">Next</span></div>

<div class="card" style="left:125px;width:305px">
  <div class="pic" role="img" aria-label="Open engine bay during engine repair" style="background:linear-gradient(135deg,#6b6b6b,#2e2e2e)"></div>
  <h3>Engine Repair</h3><p>Lorem ipsum is simply dummy text of the printing</p>
  <a>Book Now <svg width="20" height="8" viewBox="0 0 20 8" fill="none" stroke="#EB3D1F" stroke-width="1.2"><path d="M0 4h18M15 1l3 3-3 3"/></svg></a>
</div>
<div class="card" style="left:478px;width:272px">
  <div class="pic" role="img" aria-label="Car on a lift in the tire bay" style="background:linear-gradient(135deg,#b8bec4,#5f6870)"></div>
  <h3>Tires</h3><p>Lorem ipsum is simply dummy text of the printing</p>
  <a>Book Now <svg width="20" height="8" viewBox="0 0 20 8" fill="none" stroke="#EB3D1F" stroke-width="1.2"><path d="M0 4h18M15 1l3 3-3 3"/></svg></a>
</div>
<div class="card" style="left:800px;width:275px">
  <div class="pic" role="img" aria-label="Technician doing an oil change under a lifted car" style="background:linear-gradient(135deg,#3f5d8a,#c8412f)"></div>
  <h3>Oil Changes</h3><p>Lorem ipsum is simply dummy text of the printing</p>
  <a>Book Now <svg width="20" height="8" viewBox="0 0 20 8" fill="none" stroke="#EB3D1F" stroke-width="1.2"><path d="M0 4h18M15 1l3 3-3 3"/></svg></a>
</div>

<!-- GALLERY -->
<span class="eyebrow-sm center-text" style="top:2884px">OUR</span>
<h2 class="sec-title head center-text" style="top:2900px">GALLERY</h2>
<p class="center-text" style="top:2980px;font-size:12px;line-height:20px;color:#333;left:300px;width:600px">Lorem Ipsum is simply dummy text of the printing and typesetting industry. Lorem Ipsum has been the industry's standard dummy text ever since the 1500</p>
<div class="photo" role="img" aria-label="Shop building exterior under blue sky" style="left:125px;top:3064px;width:305px;height:361px;background:linear-gradient(180deg,#5f93cf 0%,#9cc1e6 55%,#6a6a6a 75%,#4a4a4a 100%)"></div>
<div class="photo" role="img" aria-label="Row of SUVs parked in front of the shop" style="left:447px;top:3064px;width:628px;height:167px;background:linear-gradient(180deg,#c9c4bb,#6d6a66)"></div>
<div class="photo" role="img" aria-label="Engine block on a workbench" style="left:447px;top:3256px;width:303px;height:169px;background:linear-gradient(135deg,#8b8b8b,#3a3a3a)"></div>
<div class="photo" role="img" aria-label="Underside of a car on a lift" style="left:772px;top:3256px;width:303px;height:361px;background:linear-gradient(160deg,#6d5a4a,#2b2622)"></div>
<div class="photo" role="img" aria-label="Engine parts in the workshop" style="left:125px;top:3447px;width:305px;height:170px;background:linear-gradient(135deg,#5a6f86,#2a2f35)"></div>
<div class="photo" role="img" aria-label="Mechanic working on suspension" style="left:447px;top:3447px;width:303px;height:170px;background:linear-gradient(135deg,#707070,#2f2f2f)"></div>
<div class="btn btn-dark" style="left:517px;top:3656px;width:166px;height:39px">See More <svg viewBox="0 0 26 10" fill="none" stroke="#fff" stroke-width="1.5"><path d="M0 5h24M20 1l4 4-4 4"/></svg></div>

<!-- CONTACT -->
<section class="contact" role="img" aria-label="Workshop interior with an SUV in the service bay"></section>
<h2 class="abs head" style="left:125px;top:4006px;color:#fff;font-size:38px;line-height:56px">Schedule<br>Appointment</h2>
<svg class="abs" style="left:125px;top:4142px" width="18" height="13" viewBox="0 0 18 13" fill="none" stroke="#EB3D1F" stroke-width="1.5"><rect x="1" y="1" width="16" height="11"/><path d="M1 1l8 6 8-6"/></svg>
<span class="abs" style="left:158px;top:4140px;color:#fff;font-size:12px">hello@varroauto.com</span>
<svg class="abs" style="left:125px;top:4180px" width="16" height="16" viewBox="0 0 16 16" fill="#EB3D1F"><path d="M3 1l3 3-2 2c1 2 3 4 5 5l2-2 3 3-2 3C7 15 1 9 1 3z"/></svg>
<span class="abs" style="left:158px;top:4179px;color:#fff;font-size:12px">555-014-2290</span>
<div class="btn btn-red" style="left:125px;top:4236px;width:167px;height:36px">Book Now <svg viewBox="0 0 26 10" fill="none" stroke="#fff" stroke-width="1.5"><path d="M0 5h24M20 1l4 4-4 4"/></svg></div>
<div class="form">
  <h2 class="head">Contact Us</h2>
  <div class="field" style="top:116px">Name</div>
  <div class="field" style="top:174px">Email Address</div>
  <div class="field" style="top:230px">Phone Number</div>
  <div class="field" style="top:290px;height:194px">Message</div>
  <div class="abs" style="left:456px;top:438px;width:40px;height:40px;background:var(--red);display:flex;align-items:center;justify-content:center">
    <svg width="18" height="18" viewBox="0 0 18 18" fill="#fff"><path d="M1 8L17 1 10 17 8 10z"/></svg>
  </div>
</div>

<!-- PARTNERS -->
<section class="partners" aria-label="Partners and certifications">
</section>
<div class="badge" style="left:125px;width:130px;background:var(--blush)"></div>
<div class="badge" style="left:318px;width:200px;top:4550px;height:36px;background:#d6efe0"></div>
<div class="badge" style="left:585px;width:190px;top:4550px;height:36px;background:var(--pink)"></div>
<div class="badge" style="left:832px;width:110px;height:90px;top:4523px;border-radius:50%;background:#e6ecf4"></div>
<div class="badge" style="left:1002px;width:70px;height:70px;top:4533px;border-radius:50%;background:#1f5fbf"></div>

<!-- FOOTER -->
<footer class="footer">
  <div class="abs" style="left:125px;top:70px;width:225px;height:200px;display:flex;align-items:center;justify-content:center;gap:10px">
    <span style="width:22px;height:22px;background:var(--red)"></span>
    <span class="head" style="font-size:34px">VARRO</span>
  </div>
  <h4 style="left:441px">QUICK LINKS</h4>
  <ul style="left:441px"><li>Home</li><li>Services</li><li>Contact Us</li><li>Gallery</li><li>Schedule Appointment</li></ul>
  <h4 style="left:674px">SERVICES</h4>
  <ul style="left:674px"><li>Oil Changes</li><li>Computer Diagnostics</li><li>Electrical Specialists</li><li>Tires</li><li>Tire Balance &amp; Rotations</li></ul>
  <h4 style="left:920px">SOCIAL MEDIA</h4>
  <ul style="left:920px"><li><span class="dot"></span>Friendsphere</li><li><span class="dot"></span>Snapgram</li><li><span class="dot"></span>Worknet</li><li><span class="dot"></span>Chirper</li></ul>
</footer>
<div class="copy">© 2024 VARRO AUTOMOTIVE. ALL RIGHTS RESERVED.</div>

</body>
</html>
```